Business card design for a world class martial arts and group fitness facility

We need a professional and eye catching design for a business card. The card will be used in networking as well as marketing.
We are a martial arts facility offering Taekwondo, Brazilian Jiu Jitsu, and group fitness. All of our programs are geared for kids and adults.
Our Taekwondo program is lead by a Hall of Fame instructor who was Instructor of the Year in 2015.
Our Brazilian Jiu Jitsu program is lead by a wold class instructor who is also a part of the renown Brazilian KLO team.
We offer 3 focused group fitness programs: Ridge kickboxing, Tandem Fitness, and The Quarry which are all lead by certified instructors in a small group setting.
Our facility is state of the art and has been recognized as such in nationally published magazines.
Our business is named The Forge which is the linear logo that is attached. This is the main logo. I also attached a circular logo we have used in some marketing material. Our Jiu Jitsu program is the KLO team logo. The Taekwondo program is the VORTEN Prime. It would be nice to somehow incorporate all 3 logos, but The Forge is most important.
We would like to use all 3 logos if possible but The Forge is the most important. We would like to have a place for a staff member's name while keeping the focus on the programs we offer.

```html
<!DOCTYPE html>
<html lang="en">
<head>
<meta charset="utf-8">
<title>The Forge — Business Card</title>
<link href="https://fonts.googleapis.com/css2?family=Raleway:wght@400;500;700;800&display=swap" rel="stylesheet">
<style>
  :root {
    --page: #e9e6e1;
    --card-dark: #111111;
    --card-dark-edge: #1e1e1e;
    --card-light: #fbfbfb;
    --ink-light: #f2f2f2;
    --ink-dark: #1b1b1b;
    --accent: #c8562a;
    --muted: #8a8a8a;
  }
  * { box-sizing: border-box; margin: 0; padding: 0; }
  html, body { width: 734px; height: 1200px; overflow: hidden; }
  body {
    background: var(--page);
    font-family: "Raleway", sans-serif;
    display: flex;
    flex-direction: column;
    align-items: center;
    justify-content: center;
    gap: 90px;
  }
  .card {
    width: 600px;
    height: 343px;
    border-radius: 18px;
    position: relative;
    box-shadow: 0 12px 30px rgba(0,0,0,.25);
  }
  /* Front */
  .card-front {
    background: linear-gradient(150deg, var(--card-dark-edge), var(--card-dark) 60%);
    color: var(--ink-light);
  }
  .partners {
    position: absolute;
    left: 40px;
    bottom: 40px;
    display: flex;
    flex-direction: column;
    gap: 28px;
  }
  .partner { display: flex; align-items: center; gap: 14px; }
  .partner-mark {
    width: 56px; height: 56px;
    border-radius: 50%;
    border: 2px solid var(--accent);
    flex: none;
  }
  .partner-name { font-weight: 700; font-size: 20px; color: var(--ink-light); }
  .tick-item { display: flex; align-items: center; gap: 8px; font-size: 14px; margin-top: 4px; }
  .tick { width: 13px; height: 13px; flex: none; }
  .emblem {
    position: absolute;
    right: 40px;
    top: 36px;
    display: flex;
    align-items: center;
    gap: 12px;
  }
  .emblem-ring { width: 46px; height: 46px; border-radius: 50%; border: 3px solid var(--accent); }
  .emblem-name { font-weight: 800; font-size: 30px; color: var(--accent); }
  .programs {
    position: absolute;
    right: 40px;
    top: 140px;
    list-style: none;
  }
  .programs-title { color: var(--accent); font-size: 15px; margin-bottom: 10px; }
  .programs li { display: flex; align-items: center; gap: 8px; font-size: 16px; margin-bottom: 8px; }
  /* Back */
  .card-back { background: var(--card-light); color: var(--ink-dark); }
  .brand {
    position: absolute;
    left: 50px; top: 60px;
    font-weight: 800;
    font-size: 76px;
    letter-spacing: -1px;
    color: var(--ink-dark);
  }
  .person { position: absolute; left: 300px; top: 170px; }
  .person-name { font-size: 28px; font-weight: 400; }
  .person-title { font-size: 12px; color: var(--accent); letter-spacing: 1px; margin-top: 2px; }
  .contacts {
    position: absolute;
    left: 50px; right: 40px; bottom: 36px;
    display: flex;
    justify-content: space-between;
    font-size: 14px;
  }
  .contact { display: flex; align-items: center; gap: 6px; }
  .contact svg { width: 13px; height: 13px; fill: var(--accent); }
</style>
</head>
<body>
  <section class="card card-front">
    <div class="emblem">
      <span class="emblem-ring"></span>
      <span class="emblem-name">The Forge</span>
    </div>
    <ul class="programs">
      <li class="programs-title">Group Fitness Programs</li>
      <li><svg class="tick" viewBox="0 0 14 14"><path d="M1 7l4 4 8-9" fill="none" stroke="#c8562a" stroke-width="2.2"/></svg>Ridge kickboxing</li>
      <li><svg class="tick" viewBox="0 0 14 14"><path d="M1 7l4 4 8-9" fill="none" stroke="#c8562a" stroke-width="2.2"/></svg>Tandem Fitness</li>
      <li><svg class="tick" viewBox="0 0 14 14"><path d="M1 7l4 4 8-9" fill="none" stroke="#c8562a" stroke-width="2.2"/></svg>The Quarry</li>
    </ul>
    <div class="partners">
      <div class="partner">
        <div>
          <div class="partner-name">VORTEN Prime</div>
          <div class="tick-item"><svg class="tick" viewBox="0 0 14 14"><path d="M1 7l4 4 8-9" fill="none" stroke="#c8562a" stroke-width="2.2"/></svg>The Taekwondo</div>
        </div>
      </div>
      <div class="partner">
        <span class="partner-mark"></span>
        <div>
          <div class="partner-name">KLO</div>
          <div class="tick-item"><svg class="tick" viewBox="0 0 14 14"><path d="M1 7l4 4 8-9" fill="none" stroke="#c8562a" stroke-width="2.2"/></svg>Jiu Jitsu program</div>
        </div>
      </div>
    </div>
  </section>

  <section class="card card-back">
    <div class="brand">The Forge</div>
    <div class="person">
      <div class="person-name">Your Name</div>
      <div class="person-title">JOB TITLE</div>
    </div>
    <div class="contacts">
      <span class="contact"><svg viewBox="0 0 14 14"><path d="M3 1h3l1 3-2 1.5a8 8 0 0 0 3.5 3.5L10 7l3 1v3a2 2 0 0 1-2 2A10 10 0 0 1 1 3a2 2 0 0 1 2-2z"/></svg>000 000 0000</span>
      <span class="contact"><svg viewBox="0 0 14 14"><path d="M1 3h12v8H1z M1 3l6 5 6-5" /></svg>Email@xyz.com</span>
      <span class="contact"><svg viewBox="0 0 14 14"><circle cx="7" cy="7" r="6"/></svg>www.website.com</span>
    </div>
  </section>
</body>
</html>
```